VORLEN Website Design

We need a website designed for our company VORLEN. We are a luxury lifestyle club that will provide benefits and services for our members. The site should be clean & sleek, preferably using black and white (or darker colors). (example sites: brimvale.example, tusko.example)

Here is a link of a sample page I did using wix. (https://pelmundry4.sitebuild.example/mypage) This can be used to get a general idea.

Target Market(s)

Upper Middle Class in the United States

Number of Pages Required

5+ page

Font styles to use
Sans Serif
Other font styles liked:
• Arial (or other similar fonts)

Requirements
Must have
• A clean design that is eye-catching and speaks to our company.
Nice to have
• Ideas for copy.

```html
<!DOCTYPE html>
<html lang="en">
<head>
<meta charset="utf-8">
<title>VORLEN — A Members Only Lifestyle Club</title>
<link rel="stylesheet" href="https://fonts.googleapis.com/css2?family=Catamaran:wght@400;500;600;700&display=swap">
<style>
  :root {
    --ink: #0a0a0a;
    --paper: #ffffff;
    --text: #1a1a1a;
    --muted: #9a9a9a;
    --frame: #d6d6d3;
    --frame-light: #dcdcdc;
    --footer: #0c0c0c;
    --footer-text: #d8d8d8;
  }
  * { box-sizing: border-box; margin: 0; padding: 0; }
  html, body { width: 1200px; height: 2189px; overflow: hidden; }
  body {
    position: relative;
    background: var(--paper);
    color: var(--text);
    font-family: "Catamaran", Arial, sans-serif;
  }
  .abs { position: absolute; }

  /* Header */
  .site-header { left: 0; top: 0; width: 1200px; height: 73px; background: var(--ink); }
  .brand { left: 117px; top: 16px; font-size: 28px; font-weight: 500; color: var(--paper); letter-spacing: 0.5px; }
  .nav-link { top: 28px; height: 29px; line-height: 29px; font-size: 12.5px; color: var(--paper); }
  .nav-link.active { border: 1px solid #8a8a8a; border-radius: 6px; padding: 0 18px; left: 793px; }

  /* Hero */
  .hero {
    left: 0; top: 73px; width: 1200px; height: 417px;
    background: radial-gradient(ellipse at 30% 40%, #5a3a22 0%, #2a1a12 40%, #120c0a 75%),
                linear-gradient(90deg, #3a2418, #1a120e);
    background-blend-mode: normal;
  }
  .hero-title {
    left: 0; top: 226px; width: 1200px; text-align: center;
    font-size: 41px; font-weight: 500; color: var(--paper);
  }

  /* About */
  .section-title { width: 1200px; left: 0; text-align: center; }
  .about-title { top: 545px; font-size: 22px; color: var(--text); }
  .about-title strong { font-size: 27px; font-weight: 600; }
  .frame-about { left: 115px; top: 629px; width: 484px; height: 352px; background: var(--frame); }
  .photo-about {
    left: 142px; top: 651px; width: 478px; height: 379px;
    background: linear-gradient(135deg, #c9b39a 0%, #8a6a52 45%, #3a2c26 100%);
  }
  .about-copy { left: 695px; top: 746px; width: 400px; font-size: 13.5px; line-height: 28px; color: var(--text); }
  .about-copy strong { font-weight: 600; }

  .btn {
    height: 41px; width: 167px; line-height: 39px; text-align: center;
    font-size: 13.5px; border-radius: 8px;
  }
  .btn-light { border: 1px solid #9a9a9a; color: var(--text); background: var(--paper); }
  .btn-dark { border: 1px solid #cfcfcf; color: var(--paper); background: rgba(0,0,0,0.35); }

  /* Benefits */
  .benefits {
    left: 0; top: 1098px; width: 1200px; height: 372px;
    background: radial-gradient(ellipse at 50% 30%, #2c2a34 0%, #17161c 55%, #0b0b10 100%);
  }
  .benefits-title { top: 1143px; font-size: 28px; font-weight: 500; color: var(--paper); letter-spacing: 0.3px; }
  .benefits-copy {
    left: 0; top: 1229px; width: 1200px; text-align: center;
    font-size: 13.5px; line-height: 28px; color: var(--paper);
  }

  /* Experiences */
  .frame-exp { left: 599px; top: 1536px; width: 486px; height: 369px; background: var(--frame-light); }
  .photo-exp {
    left: 516px; top: 1564px; width: 541px; height: 418px;
    background: radial-gradient(ellipse at 50% 40%, #3a3a7a 0%, #1a1a44 50%, #0a0a1e 100%);
  }
  .exp-title { left: 114px; top: 1646px; font-size: 27px; font-weight: 400; color: var(--text); }
  .exp-list { left: 114px; top: 1726px; width: 320px; list-style: none; }
  .exp-list li {
    position: relative; padding-left: 28px; margin-bottom: 9px;
    font-size: 13.5px; line-height: 19px; color: var(--text);
  }
  .exp-list li::before {
    content: ""; position: absolute; left: 1px; top: 4px;
    width: 10px; height: 10px; border-radius: 50%; background: var(--ink);
  }

  /* Footer */
  .site-footer { left: 0; top: 2050px; width: 1200px; height: 139px; background: var(--footer); }
  .social { top: 2103px; width: 54px; height: 54px; border: 1.5px solid #4a4a4a; border-radius: 50%; }
  .footer-link { top: 2125px; font-size: 13px; color: var(--footer-text); }
</style>
</head>
<body>

  <header class="abs site-header" aria-label="Site header"></header>
  <div class="abs brand">VORLEN</div>
  <nav aria-label="Main">
    <a class="abs nav-link active">Home</a>
    <a class="abs nav-link" style="left:898px">About</a>
    <a class="abs nav-link" style="left:967px">Services and Benefits</a>
  </nav>

  <section class="abs hero" role="img" aria-label="Photo of friends raising glasses in a toast at an evening gathering"></section>
  <h1 class="abs hero-title">A Members Only Lifestyle Club</h1>

  <h2 class="abs section-title about-title">About <strong>VORLEN</strong></h2>
  <div class="abs frame-about"></div>
  <div class="abs photo-about" role="img" aria-label="Photo of a group of friends toasting with drinks at a sunset rooftop party"></div>
  <p class="abs about-copy"><strong>VORLEN</strong> is a members only lifestyle club founded in order to bring the best services, experiences, and opportunities to our diverse community of members.<br>Our members consist of creatives, athletes, artists, and other professionals.</p>
  <a class="abs btn btn-light" style="left:806px; top:924px">Learn More</a>

  <section class="abs benefits" role="img" aria-label="Dim photo of a celebration with glasses raised under falling confetti"></section>
  <h2 class="abs section-title benefits-title">BENEFITS AND SERVICES</h2>
  <p class="abs benefits-copy">VORLEN membership provides you with amazing benefits and services.<br>Members receive access to the best accountants, attorneys, real estate agents, private bankers/advisers and more.VORLEN members also<br>receive access to private flight travel, premium luxury gym memberships, private social clubs, and private investment opportunities.</p>
  <a class="abs btn btn-dark" style="left:516px; top:1374px">Learn More</a>

  <div class="abs frame-exp"></div>
  <div class="abs photo-exp" role="img" aria-label="Photo of friends dancing under colourful stage lights and confetti at a party"></div>
  <h2 class="abs exp-title">Experiences</h2>
  <ul class="abs exp-list">
    <li>VORLEN organizes and supports a ton of private events and parties for our members.</li>
    <li>Members are also provided access to exclusive venues and events from our partners.</li>
    <li>Network with other members to build lasting relationships.</li>
  </ul>
  <a class="abs btn btn-light" style="left:185px; top:1900px">Learn More</a>

  <footer class="abs site-footer" aria-label="Site footer"></footer>
  <span class="abs social" style="left:116px" aria-label="Social link"></span>
  <span class="abs social" style="left:202px" aria-label="Social link"></span>
  <span class="abs social" style="left:287px" aria-label="Social link"></span>
  <span class="abs social" style="left:372px" aria-label="Social link"></span>
  <a class="abs footer-link" style="left:771px">About</a>
  <a class="abs footer-link" style="left:848px">Services and Benefits</a>
  <a class="abs footer-link" style="left:1016px">Contact Us</a>

</body>
</html>
```